Social Media Post Quote #4 - Native American Organization

- KINDLER - must be included
- Protect your community. Protect Your Elders. Stay Vaccinated. must be included
- Attached, company Logo, campaign logos and sample flu social media image. - our audience likes BRIGHT colors.
- Must include image from the United States, representing Land/Nature from one of the following regions, Plains and Woodlands, or Southwest, or Mountains, or Coast.
- must include quote: Our wisdom carries through generations.
- One image will be provided twice - incorporating campaign logos - in some fashion
Inspiration: https://torvelink.org/ and https://www.facebook.com/Torvelink

```html
<!DOCTYPE html>
<html lang="en">
<head>
<meta charset="utf-8">
<title>KINDLER – Our wisdom carries through generations</title>
<link rel="stylesheet" href="https://fonts.googleapis.com/css2?family=Roboto:wght@500&family=Roboto+Condensed:wght@500;700&display=swap">
<style>
  :root {
    --teal: #3a9ea6;
    --brick: #b0564b;
    --white: #ffffff;
    --forest-deep: #2f3d22;
    --forest-mid: #4f6532;
    --redwood: #9c4b27;
    --mist-top: #f6f7f3;
    --mist-low: #d9e0cf;
    --band-a: #3a9ea6;
    --band-b: #b0564b;
  }
  html, body {
    margin: 0;
    padding: 0;
    width: 1200px;
    height: 1200px;
    overflow: hidden;
    background: var(--white);
  }
  .post {
    position: relative;
    width: 1200px;
    height: 1200px;
    overflow: hidden;
  }
  .post__scene {
    position: absolute;
    inset: 0;
    width: 1200px;
    height: 1200px;
    display: block;
  }
  .campaign {
    position: absolute;
    left: 340px;
    top: 92px;
    width: 570px;
    text-align: center;
  }
  .campaign__name {
    margin: 0;
    font-family: "Roboto Condensed", sans-serif;
    font-weight: 500;
    font-size: 116px;
    line-height: 1;
    letter-spacing: 4px;
    color: var(--teal);
  }
  .campaign__caption {
    margin: 14px 0 0;
    font-family: "Roboto Condensed", sans-serif;
    font-weight: 700;
    font-size: 27px;
    letter-spacing: 1px;
    color: var(--brick);
  }
  .org {
    position: absolute;
    left: 958px;
    top: 120px;
    display: flex;
    align-items: center;
    gap: 12px;
  }
  .org__mark {
    width: 22px;
    height: 22px;
    background: var(--teal);
  }
  .org__name {
    font-family: "Roboto Condensed", sans-serif;
    font-weight: 700;
    font-size: 42px;
    color: var(--teal);
    letter-spacing: 1px;
  }
  .tagline {
    position: absolute;
    right: 20px;
    top: 352px;
    margin: 0;
    text-align: right;
    font-family: "Roboto Condensed", sans-serif;
    font-weight: 500;
    font-size: 64px;
    line-height: 76px;
    color: var(--brick);
  }
  .tagline span { display: block; }
  .quote {
    position: absolute;
    left: 14px;
    top: 735px;
    margin: 0;
    font-family: "Roboto", sans-serif;
    font-weight: 500;
    color: var(--white);
    letter-spacing: 2px;
  }
  .quote__line { display: block; }
  .quote__line--first { font-size: 118px; line-height: 128px; }
  .quote__line--second { font-size: 102px; line-height: 118px; }
  .quote__line--last { font-size: 166px; line-height: 170px; letter-spacing: 3px; }
</style>
</head>
<body>
  <main class="post">
    <svg class="post__scene" viewBox="0 0 1200 1200" xmlns="http://www.w3.org/2000/svg">
      <defs>
        <linearGradient id="forestFloor" x1="0" y1="0" x2="1" y2="0">
          <stop offset="0" stop-color="var(--forest-deep)"/>
          <stop offset="0.2" stop-color="var(--forest-mid)"/>
          <stop offset="0.38" stop-color="var(--redwood)"/>
          <stop offset="0.55" stop-color="var(--forest-mid)"/>
          <stop offset="1" stop-color="var(--forest-deep)"/>
        </linearGradient>
        <linearGradient id="forestMist" x1="0" y1="0" x2="0" y2="1">
          <stop offset="0" stop-color="var(--mist-top)"/>
          <stop offset="1" stop-color="var(--mist-low)"/>
        </linearGradient>
        <linearGradient id="bandTone" x1="0" y1="0" x2="1" y2="1">
          <stop offset="0" stop-color="var(--band-a)"/>
          <stop offset="0.5" stop-color="var(--band-b)"/>
          <stop offset="1" stop-color="var(--band-a)"/>
        </linearGradient>
      </defs>
      <polygon class="scene__forest" points="0,70 0,1200 1130,1200" fill="url(#forestFloor)"
               role="img" aria-label="Photograph of a giant redwood forest in sunlight"/>
      <polygon class="scene__forest-faded" points="70,0 1200,0 1200,1130" fill="url(#forestMist)"
               role="img" aria-label="The same redwood forest photograph, faded under a white wash"/>
      <polygon class="scene__divider" points="0,0 70,0 1200,1130 1200,1200 1130,1200 0,70" fill="url(#bandTone)"
               role="img" aria-label="Diagonal band with a teal and brick-red chevron pattern"/>
    </svg>

    <header class="campaign">
      <h1 class="campaign__name">KINDLER</h1>
      <p class="campaign__caption">COVID -19 &amp; FLU VACCINATION CAMPAIGN</p>
    </header>

    <div class="org">
      <span class="org__mark"></span>
      <span class="org__name">TORVELINK</span>
    </div>

    <p class="tagline">
      <span>Protect your community.</span>
      <span>Protect Your Elders.</span>
      <span>Stay Vaccinated.</span>
    </p>

    <blockquote class="quote">
      <span class="quote__line quote__line--first">Our wisdom</span>
      <span class="quote__line quote__line--second">carries through</span>
      <span class="quote__line quote__line--last">generations.</span>
    </blockquote>
  </main>
</body>
</html>
```